Premium men's gut health supplement needs a bottle label designed

We’re mossleaf - a premium men’s wellness brand focused on gut health. Our first product is a high-quality daily supplement designed to support digestion, regularity, and internal cleanliness. Backed by science and tailored for modern lifestyles, mossleaf is crafted in the UK and proudly LGBT-owned. It aims to resolve intimacy problems that gay men may experience due to poor digestion but also does not exclude any other orientation - other men may use it simply to improve their digestion.

mossleaf is for health-conscious men who value science-backed supplements and want to feel confident from the inside out. Many of our early adopters will be gay and bisexual men who prioritise gut health as part of their self-care, sexual, and hygiene routine, though the product is equally effective and appealing to anyone seeking premium digestive support.

The product is premium the target customer is male, not specific to one location but primary markets will be US, UK and EU.

I’d like a supplement bottle designed for mossleaf, our premium men’s gut health brand. The focus should be clean, slightly clinical, and minimal - inspired by brands like Varnō and Brek. The key element is the wordmark (mossleaf) on the front, with no additional logo or icon. Lowercase text and a strong, contemporary font are preferred.

The bottle should be aesthetically pleasing so that people are proud to display it on their shelf, instead of hiding it in a cupboard (like Varnō, brek, Ada Penrith, Olvanne etc)

Avoid anything that shows the product as being for LGBT, e.g., no rainbows, men holding hands etc.

The design should be premium, minimalist and not be busy or overwhelming.

I have uploaded a file called "Bottle" to give an idea of the type of container, but please ignore the colours and change as you see fit. This is just for reference for the type of bottle we'll use - all colours are customisable.

I have also uploaded some images for "style" reference, e.g., brek, varno, ada penrith, etc for inspiration.

```html
<!DOCTYPE html>
<html lang="en">
<head>
<meta charset="utf-8">
<title>mossleaf – pre + probiotic gut support label</title>
<link rel="stylesheet" href="https://fonts.googleapis.com/css2?family=Varela+Round&display=swap">
<style>
  :root {
    --bg: #ececec;
    --ink: #1c2626;
    --ink-soft: #3a4545;
  }
  html, body {
    margin: 0;
    padding: 0;
    width: 1200px;
    height: 900px;
    overflow: hidden;
    background: var(--bg);
  }
  .label {
    position: relative;
    width: 1200px;
    height: 900px;
    font-family: "Varela Round", "Nunito", sans-serif;
    color: var(--ink);
  }
  .wordmark {
    position: absolute;
    left: 440px;
    top: 262px;
    margin: 0;
    font-size: 78px;
    font-weight: 400;
    letter-spacing: -0.5px;
    line-height: 1;
  }
  .wordmark .reg {
    font-size: 12px;
    vertical-align: top;
    margin-left: 3px;
    position: relative;
    top: 4px;
  }
  .product-name {
    position: absolute;
    left: 442px;
    top: 532px;
    margin: 0;
    font-size: 36px;
    font-weight: 400;
    line-height: 1.1;
    letter-spacing: -0.3px;
  }
  .description {
    position: absolute;
    left: 442px;
    top: 650px;
    width: 270px;
    margin: 0;
    font-size: 12.5px;
    line-height: 1.35;
    color: var(--ink-soft);
  }
  .contents {
    position: absolute;
    left: 442px;
    top: 764px;
    margin: 0;
    font-size: 15px;
    line-height: 1.25;
  }
</style>
</head>
<body>
  <main class="label">
    <h1 class="wordmark">mossleaf<span class="reg">®</span></h1>
    <h2 class="product-name">pre + probiotic<br>gut support</h2>
    <p class="description">daily wellness supplement for improving digestion, support regularity, immaculacy and overall gut health.</p>
    <p class="contents">dietary supplement<br>60 soft gels</p>
  </main>
</body>
</html>
```